BUSINESS CONSULTING

Would like a page design that would reflect "flow" effect that denotes moving around obstacles and logo webpage for Brenmark Consulting. We provide business consulting in the areas of training/facilitation, Leadership Coaching and Development, Process Improvement and Employee On-boarding and Authorization.

Need skeletal designed to be populated at a later date.

Industry/Entity Type

Business

```html
<!DOCTYPE html>
<html lang="en">
<head>
<meta charset="utf-8">
<title>BRENMARK Consulting</title>
<link href="https://fonts.googleapis.com/css2?family=PT+Sans+Narrow:wght@400;700&family=Open+Sans:wght@400;600&display=swap" rel="stylesheet">
<style>
:root{
  --green:#1a9a3c;
  --green-dark:#14772f;
  --ink:#4a4f58;
  --body:#5c5f63;
  --muted:#8a8d90;
  --nav:#5a6068;
  --panel:#f1f3f2;
  --footer:#ebebeb;
  --card-top:#8c8f92;
}
*{box-sizing:border-box;margin:0;padding:0}
html,body{width:1024px;height:1200px;overflow:hidden}
body{position:relative;background:var(--panel);font-family:"Open Sans",sans-serif;color:var(--body)}
.abs{position:absolute}

/* header */
.site-header{left:0;top:0;width:1024px;height:83px;background:#fff;border-top:3px solid #cfd2d4}
.inquiry{left:604px;top:0;width:288px;height:26px;background:#f0f1f1;border-radius:0 0 10px 10px;font:700 12px "PT Sans Narrow",sans-serif;color:var(--nav);display:flex;align-items:center;gap:6px;padding-left:12px}
.inquiry strong{color:var(--green)}
.brand{left:116px;top:28px;font:700 24px "PT Sans Narrow",sans-serif;color:var(--green);letter-spacing:-.3px}
.main-nav{left:494px;top:45px;display:flex;gap:28px;font:700 12px "PT Sans Narrow",sans-serif;color:var(--nav);letter-spacing:.6px}
.main-nav .active{color:#2f3440}
.quote-btn{left:775px;top:35px;width:112px;height:36px;background:linear-gradient(#f8ab3a,#ee8b14);border-radius:3px;border:1px solid #dc7f10;color:#fff;font:700 11px/12px "PT Sans Narrow",sans-serif;letter-spacing:.6px;display:flex;align-items:center;gap:8px;padding-left:13px}

/* hero */
.hero{left:0;top:83px;width:1024px;height:397px;background:linear-gradient(100deg,#3f7a2e 0%,#6aa13c 25%,#4b5553 45%,#8f98a0 70%,#7a848d 100%)}
.hero-arrow{width:38px;height:38px;border-radius:50%;border:3px solid #d8dcdc;display:flex;align-items:center;justify-content:center}
.hero-arrow.prev{left:77px;top:235px;background:var(--green)}
.hero-arrow.next{left:903px;top:235px;background:#3e4246}
.hero-title{left:112px;top:334px;font:700 33px/41px "PT Sans Narrow",sans-serif;color:#fff;letter-spacing:-.5px;text-shadow:0 1px 3px rgba(0,0,0,.4)}

/* feature panel */
.feature-panel{left:108px;top:439px;width:803px;height:305px;background:var(--panel);border-radius:3px;box-shadow:0 10px 20px rgba(0,0,0,.08)}
.card{top:470px;width:177px;height:233px;background:#fff;border-top:4px solid var(--card-top);box-shadow:0 1px 3px rgba(0,0,0,.18)}
.card h3{position:absolute;left:0;top:18px;width:100%;text-align:center;font:700 11px/14px "PT Sans Narrow",sans-serif;color:var(--green)}
.card .photo{position:absolute;left:14px;top:48px;width:149px;height:78px}
.card p{position:absolute;left:14px;top:148px;width:144px;font-size:8.4px;line-height:11.2px;color:#4a4a4a}
.card a{position:absolute;left:14px;top:205px;font-size:7.6px;color:#3b5a8a;text-decoration:underline;letter-spacing:.3px}

/* welcome */
.welcome-photo{left:136px;top:757px;width:158px;height:210px;background:linear-gradient(160deg,#8fa7b3 0%,#9ab08a 40%,#5f8f6a 65%,#4f5a58 100%)}
.section-title{font:700 19px "PT Sans Narrow",sans-serif;color:var(--ink)}
.section-title span{color:var(--green)}
.welcome-title{left:311px;top:749px}
.welcome-text{left:312px;top:784px;width:296px;font-size:9.6px;line-height:16px;color:var(--body)}
.welcome-text p+p{margin-top:16px}
.learn-btn{left:311px;top:938px;width:64px;height:28px;border:1px solid #c9cbcc;border-radius:3px;background:linear-gradient(#f7f7f7,#e4e5e5);font-size:8.5px;color:#777;display:flex;align-items:center;justify-content:center}
.services-title{left:649px;top:749px}
.service-list{left:649px;top:785px;list-style:none}
.service-list li{display:flex;align-items:center;gap:10px;height:24px;font-size:11.8px;color:var(--ink)}

/* footer */
.site-footer{left:0;top:1017px;width:1024px;height:147px;background:var(--footer);border-top:1px solid #dcdcdc}
.footer-brand{left:153px;top:1071px;font:700 15px "PT Sans Narrow",sans-serif;color:var(--green)}
.footer-col{top:1041px}
.footer-col h4{font:600 11.5px "Open Sans",sans-serif;color:#5a5e62;margin-bottom:9px}
.footer-col ul{list-style:none}
.footer-col li{font-size:8.6px;color:var(--muted);height:19px;display:flex;align-items:center;gap:7px}
.footer-col li .caret{width:0;height:0;border-left:3px solid #9a9c9e;border-top:3px solid transparent;border-bottom:3px solid transparent}
.footer-col li.current{color:var(--green)}
.contact-list li{height:24px;gap:10px}
.social{display:flex;gap:9px}
.social span{width:28px;height:28px;border-radius:3px;box-shadow:0 1px 2px rgba(0,0,0,.3)}
.bottom-bar{left:0;top:1164px;width:1024px;height:36px;background:var(--green-dark);font-size:8.5px;color:#6cb77d}
.bottom-bar .copy{position:absolute;left:134px;top:13px}
.bottom-bar .legal{position:absolute;right:138px;top:13px;display:flex;gap:10px}
</style>
</head>
<body>

<header class="abs site-header"></header>
<div class="abs inquiry">
  <svg width="16" height="16" viewBox="0 0 16 16"><circle cx="8" cy="8" r="7" fill="none" stroke="#1a9a3c" stroke-width="1.4"/><path d="M5.2 4.6c.6-.4 1 .1 1.3.7l.3.6c.2.4 0 .7-.3.9-.2.2-.2.5 0 .8.4.7.9 1.2 1.6 1.6.3.2.6.2.8 0 .2-.3.5-.5.9-.3l.6.3c.6.3 1.1.7.7 1.3-.7 1-2 1.1-3.3.2-1.2-.8-2.1-1.7-2.9-2.9-.8-1.3-.7-2.6.3-3.2z" fill="#1a9a3c"/></svg>
  FOR INQUIRIES, CALL US: <strong>1-800-555-0142</strong>
</div>
<div class="abs brand">BRENMARK Consulting</div>
<nav class="abs main-nav">
  <span class="active">HOME</span><span>ABOUT US</span><span>SERVICES</span><span>CONTACT</span>
</nav>
<div class="abs quote-btn">
  <svg width="16" height="20" viewBox="0 0 16 20"><path d="M1 1h10l4 4v14H1z" fill="none" stroke="#fff" stroke-width="1.5"/><path d="M4 8h8M4 11h8M4 14h8" stroke="#fff" stroke-width="1.4"/></svg>
  <span>BOOK YOUR<br>FREE CONSULT</span>
</div>

<section class="abs hero" role="img" aria-label="Photo of a team moving forward together, with soft motion blur suggesting flow around obstacles"></section>
<div class="abs hero-arrow prev"><svg width="8" height="10" viewBox="0 0 8 10"><path d="M5.5 2L2.5 5l3 3" fill="none" stroke="#fff" stroke-width="1.5"/></svg></div>
<div class="abs hero-arrow next"><svg width="8" height="10" viewBox="0 0 8 10"><path d="M2.5 2l3 3-3 3" fill="none" stroke="#fff" stroke-width="1.5"/></svg></div>
<h1 class="abs hero-title">Helping Your Business Flow<br>Around Every Obstacle</h1>

<div class="abs feature-panel"></div>

<article class="abs card" style="left:134px">
  <h3>Training &amp;<br>Facilitation</h3>
  <div class="photo" role="img" aria-label="Photo of a facilitator leading a workshop" style="background:linear-gradient(135deg,#1d4f8f,#4a9ad6 50%,#163a6a)"></div>
  <p>Lorem ipsum dolor sit amet, consectetur adipisicing elit, sed do eiusmod tempor incididunt ut labore .</p>
  <a>READ MORE</a>
</article>
<article class="abs card" style="left:326px">
  <h3>Process Improvement &amp;<br>Consulting</h3>
  <div class="photo" role="img" aria-label="Photo of business colleagues reviewing work at a laptop" style="background:linear-gradient(135deg,#e9ecec,#b7bcbf 55%,#3a3d42)"></div>
  <p>Lorem ipsum dolor sit amet, consectetur adipisicing elit, sed do eiusmod tempor incididunt ut labore .</p>
  <a>READ MORE</a>
</article>
<article class="abs card" style="left:518px">
  <h3>Leadership Coaching &amp;<br>Development</h3>
  <div class="photo" role="img" aria-label="Photo of a coaching session between two managers" style="background:linear-gradient(90deg,#2f6b45,#6aa13c 40%,#c9d2b8 75%,#8a9296)"></div>
  <p>Lorem ipsum dolor sit amet, consectetur adipisicing elit, sed do eiusmod tempor incididunt ut labore .</p>
  <a>READ MORE</a>
</article>
<article class="abs card" style="left:710px">
  <h3>Employee On-boarding &amp;<br>Authorization</h3>
  <div class="photo" role="img" aria-label="Photo of hands signing onboarding documents beside a keyboard" style="background:linear-gradient(135deg,#f2f2f2,#cfc8c0 50%,#5a5a5c)"></div>
  <p>Lorem ipsum dolor sit amet, consectetur adipisicing elit, sed do eiusmod tempor incididunt ut labore .</p>
  <a>READ MORE</a>
</article>

<div class="abs welcome-photo" role="img" aria-label="Photo of a consultant meeting with a client team"></div>
<h2 class="abs section-title welcome-title">Welcome to <span>BRENMARK Consulting</span></h2>
<div class="abs welcome-text">
  <p>It is a long established fact that a reader will be distracted by the readable content of a page when looking at its layout. The point of using Lorem Ipsum is that it has a more-or-less normal distribution of letters, as opposed to using 'Content here, content here', making it look like readable English.</p>
  <p>Lorem ipsum dolor sit amet, consectetur adipisicing elit, sed do eiusmod tempor incididunt ut labore et dolore magna aliqua. Ut enim ad minim veniam, quis nostrud exercitation ullamco laboris</p>
</div>
<div class="abs learn-btn">Learn More</div>

<h2 class="abs section-title services-title">Our <span>Services</span></h2>
<ul class="abs service-list">
  <li><svg width="15" height="15" viewBox="0 0 15 15"><circle cx="7.5" cy="7.5" r="7.5" fill="#1a9a3c"/><path d="M6 4.5l3 3-3 3" fill="none" stroke="#fff" stroke-width="1.6"/></svg>Training and Facilitation</li>
  <li><svg width="15" height="15" viewBox="0 0 15 15"><circle cx="7.5" cy="7.5" r="7.5" fill="#1a9a3c"/><path d="M6 4.5l3 3-3 3" fill="none" stroke="#fff" stroke-width="1.6"/></svg>Leadership Coaching</li>
  <li><svg width="15" height="15" viewBox="0 0 15 15"><circle cx="7.5" cy="7.5" r="7.5" fill="#1a9a3c"/><path d="M6 4.5l3 3-3 3" fill="none" stroke="#fff" stroke-width="1.6"/></svg>Leadership Development</li>
  <li><svg width="15" height="15" viewBox="0 0 15 15"><circle cx="7.5" cy="7.5" r="7.5" fill="#1a9a3c"/><path d="M6 4.5l3 3-3 3" fill="none" stroke="#fff" stroke-width="1.6"/></svg>Process Improvement Consulting</li>
  <li><svg width="15" height="15" viewBox="0 0 15 15"><circle cx="7.5" cy="7.5" r="7.5" fill="#1a9a3c"/><path d="M6 4.5l3 3-3 3" fill="none" stroke="#fff" stroke-width="1.6"/></svg>Workflow and Change Management</li>
  <li><svg width="15" height="15" viewBox="0 0 15 15"><circle cx="7.5" cy="7.5" r="7.5" fill="#1a9a3c"/><path d="M6 4.5l3 3-3 3" fill="none" stroke="#fff" stroke-width="1.6"/></svg>Employee On-boarding</li>
  <li><svg width="15" height="15" viewBox="0 0 15 15"><circle cx="7.5" cy="7.5" r="7.5" fill="#1a9a3c"/><path d="M6 4.5l3 3-3 3" fill="none" stroke="#fff" stroke-width="1.6"/></svg>Employee Authorization</li>
  <li><svg width="15" height="15" viewBox="0 0 15 15"><circle cx="7.5" cy="7.5" r="7.5" fill="#1a9a3c"/><path d="M6 4.5l3 3-3 3" fill="none" stroke="#fff" stroke-width="1.6"/></svg>Team Workshops</li>
</ul>

<footer class="abs site-footer"></footer>
<div class="abs footer-brand">BRENMARK Consulting</div>
<div class="abs footer-col" style="left:321px">
  <h4>Navigation</h4>
  <ul><li><i class="caret"></i>Home</li><li><i class="caret"></i>About</li><li><i class="caret"></i>Services</li><li><i class="caret"></i>Contact</li></ul>
</div>
<div class="abs footer-col" style="left:448px">
  <h4>Services</h4>
  <ul><li class="current"><i class="caret"></i>Service</li><li><i class="caret"></i>Service</li><li><i class="caret"></i>Service</li><li><i class="caret"></i>Service</li></ul>
</div>
<div class="abs footer-col" style="left:577px">
  <h4>Contact Us</h4>
  <ul class="contact-list">
    <li><svg width="10" height="10" viewBox="0 0 10 10"><path d="M1.5 1c.8-.6 1.3 0 1.7.8l.3.6c.2.5-.1.8-.4 1-.2.2-.2.5 0 .9.5.8 1 1.3 1.8 1.8.4.2.7.2.9 0 .2-.3.5-.6 1-.4l.6.3c.8.4 1.4.9.8 1.7-.9 1.2-2.5 1.3-4 .2C2.7 6.9 1.8 6 1.1 4.8.2 3.3.3 1.8 1.5 1z" fill="#9a9c9e"/></svg>+1-800-555-0176</li>
    <li><svg width="12" height="9" viewBox="0 0 12 9"><rect x=".5" y=".5" width="11" height="8" fill="#9a9c9e"/><path d="M.5.5l5.5 4.5L11.5.5" fill="none" stroke="#ebebeb" stroke-width="1"/></svg>info@yourwebsite.com</li>
    <li style="align-items:flex-start;height:auto;line-height:19px"><svg width="9" height="12" viewBox="0 0 9 12" style="margin-top:3px"><path d="M4.5 0C2 0 0 2 0 4.4 0 7.5 4.5 12 4.5 12S9 7.5 9 4.4C9 2 7 0 4.5 0z" fill="#9a9c9e"/><circle cx="4.5" cy="4.4" r="1.6" fill="#ebebeb"/></svg><span>Your Address, Your Country<br>Your Zip Code</span></li>
  </ul>
</div>
<div class="abs footer-col" style="left:750px">
  <h4>Social</h4>
  <div class="social">
    <span style="background:#3a5a9a" role="img" aria-label="Social network link"></span>
    <span style="background:#2a9ad8" role="img" aria-label="Social network link"></span>
    <span style="background:#1a6fa8" role="img" aria-label="Social network link"></span>
    <span style="background:#d23a2c" role="img" aria-label="Social network link"></span>
  </div>
</div>

<div class="abs bottom-bar">
  <span class="copy">Copyright 2014 © Brenmark Consulting - All Rights Reserved</span>
  <span class="legal"><span>Site Map</span><span>•</span><span>Privacy Policy</span></span>
</div>

</body>
</html>
```